Spa Business Card Design Project

Hello! We are a boutique spa for men and women that is rebranding. I would like a memorable new business card that showcases our beautiful new logo and our unique business. I would like it to be classic/timeless and eclectic/artistic at the  same time.
I am a fan of negative space as you can tell from the logo. I am also open to any creative ideas.
Multi sided design. Two sided design is acceptable as an option, too. "Flaps/folds/whatever the design term is" are optional- whether full vertical or horizontal, half flap, full flap etc
On either side next to the golden snail I would potentially like to see "Take it slow. Savor Life."  Possibly on one statment on top of each other, crowned with the snail. Or the statment following the snail on one line... I am open for a creative suprise, too.
The back I would like room for the standard Information
"3817 Birch Lane
Harlow Falls, Vermont 05301
(518) 462 3085
info@thecorvella spa.com
The snail is to be done in gold ink.
Can I also Have an option for cards that are individualized for staff members, too?

Updates
Project Deadline Extended
Reason: I apologize for the deadline extension. My day was more involved than anticipated in other matters. Hope to have this closed by next Tuesday.
Thank you

Target Market(s)
Men and women with expendable income between the ages of 30-55
Industry/Entity Type
Boutique
Requirements
Must have
- only black and gold ink.

Nice to have
- One of a kind.
Showcase the snail :-)
make you smile :-)
Fun, but professional.
Should not have
- Lots of color.
Too feminine.
Too busy.

```html
<!DOCTYPE html>
<html lang="en">
<head>
<meta charset="utf-8">
<title>Staff Business Card – Rosalinde</title>
<link rel="stylesheet" href="https://fonts.googleapis.com/css2?family=Josefin+Sans:wght@300&family=Open+Sans:wght@500&family=Cormorant+Garamond:ital,wght@1,600&display=swap">
<style>
  :root {
    --card-black: #060807;
    --gold: #a8890e;
  }
  * { margin: 0; padding: 0; box-sizing: border-box; }
  html, body {
    width: 1200px;
    height: 741px;
    overflow: hidden;
    background: var(--card-black);
  }
  .card {
    position: relative;
    width: 1200px;
    height: 741px;
    background: var(--card-black);
    color: var(--gold);
  }
  .staff-name {
    position: absolute;
    top: 122px;
    left: 0;
    width: 100%;
    text-align: center;
    font-family: "Josefin Sans", sans-serif;
    font-weight: 300;
    font-size: 54px;
    letter-spacing: 0;
    line-height: 1;
  }
  .name-rule {
    position: absolute;
    top: 206px;
    left: 459px;
    width: 282px;
    height: 6px;
  }
  .contact-icon {
    position: absolute;
  }
  .icon-mail { left: 389px; top: 288px; width: 52px; height: 38px; }
  .icon-phone { left: 395px; top: 367px; width: 41px; height: 50px; }
  .icon-web { left: 401px; top: 454px; width: 27px; height: 44px; }
  .contact-text {
    position: absolute;
    font-family: "Open Sans", sans-serif;
    font-weight: 500;
    font-size: 23px;
    letter-spacing: 1px;
    line-height: 31px;
    white-space: nowrap;
  }
  .contact-address { left: 489px; top: 276px; }
  .contact-phone { left: 484px; top: 375px; }
  .contact-email { left: 482px; top: 460px; }
  .tagline {
    position: absolute;
    top: 626px;
    left: 0;
    width: 100%;
    text-align: center;
    font-family: "Cormorant Garamond", serif;
    font-style: italic;
    font-weight: 600;
    font-size: 40px;
    letter-spacing: 2px;
    line-height: 1;
  }
</style>
</head>
<body>
  <main class="card">
    <h1 class="staff-name">ROSALINDE</h1>
    <svg class="name-rule" viewBox="0 0 282 6" aria-hidden="true">
      <path d="M0 3 Q141 0 282 3 Q141 6 0 3 Z" fill="var(--gold)"/>
    </svg>

    <svg class="contact-icon icon-mail" viewBox="0 0 52 38" aria-hidden="true">
      <rect x="2" y="2" width="48" height="34" fill="none" stroke="var(--gold)" stroke-width="3"/>
      <path d="M3 3 L26 22 L49 3 M3 35 L20 17 M49 35 L32 17" fill="none" stroke="var(--gold)" stroke-width="3"/>
    </svg>
    <p class="contact-text contact-address">3817 Birch Lane<br>Harlow Falls, Vermont 05301</p>

    <svg class="contact-icon icon-phone" viewBox="0 0 41 50" aria-hidden="true">
      <path d="M8 2 L15 0 L19 13 L13 17 Q14 28 23 37 L29 33 L38 42 L33 48 Q22 51 12 38 Q2 24 3 10 Z" fill="var(--gold)"/>
    </svg>
    <p class="contact-text contact-phone">(518) 462 3085</p>

    <svg class="contact-icon icon-web" viewBox="0 0 27 44" aria-hidden="true">
      <path d="M1 0 L26 24 L16 25 L22 41 L17 43 L11 27 L3 33 Z" fill="var(--gold)"/>
    </svg>
    <p class="contact-text contact-email">info@thecorvella spa.com</p>

    <p class="tagline">Take it slow. Savor Life</p>
  </main>
</body>
</html>
```